Bytemill - a software development company requires letter head

I currently have a business card and logo, I just need a nice looking letter head the matches the two. I will upload these Illustrator files.

I would like the letter head to be done in a current version of MS Word.

Please incorporate 'bytemill' as per the attached font and the logo.

Industry/Entity Type

Computer Software

Colors

Designer to choose colors to be used in the design.

Requirements
Must have
• Fits in with current design, sleek and professional. It will be used for quotations and tenders and documentation going to clients and potential clients.
• Would like to company logo up the top header and perhaps a watermark of the logo at the bottom right, a bit like the business card.
• Also it needs to be MS word.
• Please work with the color pallet from the attached files.

```html
<!DOCTYPE html>
<html lang="en">
<head>
<meta charset="utf-8">
<title>Bytemill Letterhead</title>
<link href="https://fonts.googleapis.com/css2?family=Open+Sans:wght@400;600&display=swap" rel="stylesheet">
<style>
  :root {
    --backdrop: #6f6f6f;
    --paper: #fafafa;
    --brand-blue: #29a8e0;
    --ink: #4a4a4a;
    --watermark-blue: #dbeef8;
  }
  * { margin: 0; padding: 0; box-sizing: border-box; }
  html, body {
    width: 1200px;
    height: 1006px;
    overflow: hidden;
    background: var(--backdrop);
    font-family: "Open Sans", sans-serif;
  }
  .letterhead {
    position: absolute;
    left: 211px;
    top: 0;
    width: 778px;
    height: 1006px;
    background: var(--paper);
    overflow: hidden;
  }
  .brand {
    position: absolute;
    left: 77px;
    top: 66px;
    display: flex;
    flex-direction: column;
    align-items: center;
    gap: 12px;
    width: 168px;
  }
  .brand-dot {
    width: 52px;
    height: 52px;
    border-radius: 50%;
    background: var(--brand-blue);
  }
  .brand-name {
    font-size: 25px;
    font-weight: 600;
    letter-spacing: 1.5px;
    text-transform: uppercase;
    color: var(--ink);
    line-height: 1;
  }
  .watermark {
    position: absolute;
    right: -140px;
    bottom: -120px;
    width: 400px;
    height: 400px;
    border-radius: 50%;
    background: var(--watermark-blue);
  }
  .footer-tab {
    position: absolute;
    left: 0;
    top: 897px;
    width: 25px;
    height: 70px;
    background: var(--brand-blue);
    border-radius: 0 6px 6px 0;
  }
  .address {
    position: absolute;
    left: 52px;
    top: 897px;
    font-size: 10.5px;
    line-height: 12.5px;
    color: var(--ink);
  }
  .contact-list {
    position: absolute;
    left: 52px;
    top: 930px;
    list-style: none;
    font-size: 10.5px;
    line-height: 12.5px;
    color: var(--ink);
  }
  .contact-list li {
    display: flex;
    align-items: center;
    gap: 7px;
  }
  .contact-icon {
    width: 9px;
    height: 9px;
    flex: none;
  }
</style>
</head>
<body>
  <main class="letterhead">
    <header class="brand">
      <span class="brand-dot"></span>
      <span class="brand-name">Bytemill</span>
    </header>

    <div class="watermark" aria-hidden="true"></div>

    <footer>
      <span class="footer-tab"></span>
      <address class="address" style="font-style:normal">
        48 Harbor Lane, Suite 12<br>
        Westfield, CA 90210.
      </address>
      <ul class="contact-list">
        <li>
          <svg class="contact-icon" viewBox="0 0 10 10"><path d="M2 1 L4 1 L4.6 3 L3.4 3.8 Q4.4 5.8 6.2 6.6 L7 5.4 L9 6 L9 8 Q5 9 2 5.5 Q1 3.5 2 1 Z" fill="var(--brand-blue)"/></svg>
          +1 555 014 7781
        </li>
        <li>
          <svg class="contact-icon" viewBox="0 0 10 10"><rect x="0.5" y="2" width="9" height="6.5" rx="1" fill="var(--brand-blue)"/><path d="M1 2.6 L5 5.6 L9 2.6" stroke="#fff" stroke-width="0.9" fill="none"/></svg>
          info@bytemill.com
        </li>
        <li>
          <svg class="contact-icon" viewBox="0 0 10 10"><circle cx="5" cy="5" r="4.2" fill="none" stroke="var(--brand-blue)" stroke-width="1"/><ellipse cx="5" cy="5" rx="1.8" ry="4.2" fill="none" stroke="var(--brand-blue)" stroke-width="0.8"/><path d="M1 5 H9" stroke="var(--brand-blue)" stroke-width="0.8"/></svg>
          www.bytemill.com
        </li>
      </ul>
    </footer>
  </main>
</body>
</html>
```